Serial Entrepreneur Business Card: 4 Logo Design

I am a serial entrepreneur and a full time mechanical engineer. I have four businesses. I would like to display them all on one business card.
*Please see the attached PDF for the design requirements*

www.KelbroNest.com

Businesses
-KelbroNest
-Quiet Lantern Properties
-Torlen Products
-Drosk Harbor Cast

Target Market(s)

Clients, Entrepreneurs, Associates, really anyone. Should be very professional.

Industry/Entity Type

Entrepreneur

Contact Information for Business Card

3.5" x 2" Standard Business Card Size
** Please review the attached requirement PDF for in depth detail on what I am expecting**

Font styles to use
Sans Serif

Requirements
Must have
• My personal contact information:
• First Name: Dae hwan
• Last Name: Pellow
• Nick Name: Riko
• Address: 83 Tolmer Court, Garfield NJ 07392
• Phone Number: 201-574-2916
• Email: RikodPellow@mailnest.example
• Website: www.KelbroNest.com
• All Four Logos of the Companies I own:
• -KelbroNest
• -Quiet Lantern Properties
• -Torlen Products
• -Drosk Harbor Cast
• My Professions:
• -Prototyping Engineer
• -Real Estate Investor
• -Financial Blogger
• -Video Podcaster
• -Online Retail Seller
Nice to have
• If it fits, please include the website for each logo, if there is more space please include the email for each.
• It might be nice to have the QX GUILD Logo, or TOVRA logo for my full-time job. But only if it fits.

```html
<!DOCTYPE html>
<html lang="en">
<head>
<meta charset="utf-8">
<title>Dae hwan "Riko" Pellow – Business Card</title>
<link rel="stylesheet" href="https://fonts.googleapis.com/css2?family=Roboto+Condensed:wght@400;700&display=swap">
<style>
  :root {
    --backdrop: #e9dcc6;
    --silver-light: #ffffff;
    --silver-mid: #e6e6e6;
    --silver-dark: #b9b9b9;
    --brand-green: #0b8a12;
    --ink: #2b2b2b;
    --ink-soft: #3c3c3c;
    --font: "Roboto Condensed", Arial, sans-serif;
  }
  * { margin: 0; padding: 0; box-sizing: border-box; }
  html, body { width: 985px; height: 1200px; overflow: hidden; }
  body { background: var(--backdrop); font-family: var(--font); color: var(--ink); position: relative; }

  .card {
    position: absolute;
    background: linear-gradient(90deg, var(--silver-dark) 0%, var(--silver-mid) 18%, var(--silver-light) 42%, var(--silver-light) 62%, var(--silver-mid) 85%, var(--silver-dark) 100%);
    box-shadow: 0 2px 6px rgba(0,0,0,.25);
    overflow: hidden;
  }
  .card--front { left: 98px; top: 88px; width: 775px; height: 455px; }
  .card--back  { left: 102px; top: 657px; width: 773px; height: 457px; }

  .card__sheen {
    position: absolute; left: 0; right: 0; height: 12px;
    background: linear-gradient(90deg, #9e9e9e, #f4f4f4 30%, #8c8c8c 60%, #f0f0f0 85%, #a5a5a5);
  }
  .card__band { position: absolute; left: 0; right: 0; bottom: 0; height: 42px; background: var(--brand-green); }

  .abs { position: absolute; }
  .center { transform: translate(-50%, -50%); text-align: center; white-space: nowrap; }
  .mid-left { transform: translateY(-50%); white-space: nowrap; }

  .owner-name { font-weight: 700; font-size: 20px; letter-spacing: .3px; color: var(--ink); text-transform: uppercase; }
  .contact-line { font-weight: 700; font-size: 19px; color: var(--ink); display: flex; align-items: center; gap: 10px; }
  .contact-line svg { flex: none; }

  .role-label { font-weight: 700; font-size: 16px; color: var(--ink); }
  .role-email { font-size: 15.5px; color: var(--ink-soft); }

  .brand-mark { display: flex; align-items: center; gap: 7px; font-weight: 700; font-size: 22px; }
  .brand-mark__square { width: 14px; height: 14px; background: var(--brand-green); flex: none; }
  .brand-mark--dark { color: var(--ink); }
  .brand-mark--green { color: var(--brand-green); }
  .brand-mark--large { font-size: 27px; gap: 9px; }
  .brand-mark--large .brand-mark__square { width: 18px; height: 18px; }

  .brand-url { font-weight: 700; font-size: 17px; color: var(--ink); }

  .profession-list { list-style: none; }
  .profession-list li { font-size: 17.5px; color: var(--ink-soft); line-height: 26px; display: flex; align-items: center; }
  .profession-list li::before { content: ""; width: 6px; height: 6px; border-radius: 50%; background: var(--brand-green); margin-right: 9px; }
</style>
</head>
<body>

<section class="card card--front" aria-label="Business card front">
  <div class="abs center brand-mark brand-mark--dark" style="left:155px; top:104px;"><span class="brand-mark__square"></span>KelbroNest</div>
  <div class="abs center role-label" style="left:155px; top:177px;">Financial Blogger</div>
  <div class="abs center role-email" style="left:155px; top:198px;">Riko@KelbroNest.com</div>

  <div class="abs mid-left owner-name" style="left:284px; top:88px;">Dae hwan «Riko» Pellow</div>
  <div class="abs mid-left contact-line" style="left:284px; top:134px;">
    <svg width="18" height="26" viewBox="0 0 18 26" aria-hidden="true"><path d="M9 1a8 8 0 0 0-8 8c0 6 8 15 8 15s8-9 8-15a8 8 0 0 0-8-8z" fill="var(--brand-green)"/><circle cx="9" cy="9" r="3.2" fill="#fff"/></svg>
    83 Tolmer Court, Halvern ZT 07392
  </div>
  <div class="abs mid-left contact-line" style="left:284px; top:172px;">
    <svg width="18" height="26" viewBox="0 0 18 26" aria-hidden="true"><rect x="2" y="1" width="14" height="24" rx="2.5" fill="none" stroke="var(--brand-green)" stroke-width="2.4"/><rect x="5" y="5" width="8" height="13" fill="var(--brand-green)"/><circle cx="9" cy="21" r="1.4" fill="var(--brand-green)"/></svg>
    201-574-2916
  </div>

  <div class="abs center brand-mark brand-mark--dark" style="left:155px; top:285px;"><span class="brand-mark__square"></span>Quiet Lantern</div>
  <div class="abs center brand-mark brand-mark--green" style="left:401px; top:290px;"><span class="brand-mark__square"></span>Drosk Harbor</div>
  <div class="abs center brand-mark brand-mark--dark" style="left:631px; top:290px;"><span class="brand-mark__square"></span>Torlen</div>

  <div class="abs center role-label" style="left:155px; top:345px;">Real Estate Investing</div>
  <div class="abs center role-email" style="left:155px; top:367px;">Riko@QuietLanternProperties.com</div>
  <div class="abs center role-label" style="left:401px; top:345px;">Vlogger</div>
  <div class="abs center role-email" style="left:401px; top:367px;">Media@DroskHarborCast.com</div>
  <div class="abs center role-label" style="left:631px; top:345px;">Online Retail Seller</div>
  <div class="abs center role-email" style="left:631px; top:367px;">Sales@TorlenProducts.com</div>

  <div class="card__sheen" style="top:401px;"></div>
  <div class="card__band"></div>
</section>

<section class="card card--back" aria-label="Business card back">
  <div class="abs mid-left owner-name" style="left:79px; top:85px;">Dae hwan «Riko» Pellow</div>
  <ul class="abs profession-list" style="left:79px; top:103px;">
    <li>Prototyping Engineer</li>
    <li>Real Estate Investor</li>
    <li>Financial Blogger</li>
    <li>Video Podcaster</li>
    <li>Online Retail Seller</li>
  </ul>

  <div class="abs center brand-mark brand-mark--large brand-mark--dark" style="left:172px; top:310px;"><span class="brand-mark__square"></span>Torlen Products</div>
  <div class="abs center brand-url" style="left:172px; top:378px;">www.TorlenProducts.com</div>

  <div class="abs center brand-mark brand-mark--large brand-mark--dark" style="left:573px; top:86px;"><span class="brand-mark__square"></span>KelbroNest</div>
  <div class="abs center brand-url" style="left:573px; top:123px;">www.KelbroNest.com</div>

  <div class="abs center brand-mark brand-mark--large brand-mark--dark" style="left:573px; top:196px;"><span class="brand-mark__square"></span>Quiet Lantern Properties</div>
  <div class="abs center brand-url" style="left:573px; top:243px;">www.QuietLanternProperties.com</div>

  <div class="abs center brand-mark brand-mark--large brand-mark--green" style="left:573px; top:325px;"><span class="brand-mark__square"></span>Drosk Harbor Cast</div>
  <div class="abs center brand-url" style="left:573px; top:377px;">www.DroskHarborCast.com</div>

  <div class="card__sheen" style="top:403px;"></div>
  <div class="card__band"></div>
</section>

</body>
</html>
```